Bref créative
Stationary Package - Paper, Envelope, Fax Cover, Bus. Card
Mortgage Co. seeks Stationary Package
Professional
Marla Henson
Broker / Owner
246 W. "K" Avenue
Cedarmont CA 91704
MarlaHenson@quillmail.example
DRE LIC 05837162 NMLS 489153
Head Shot Photo on Front about a 1/3 of the card to 1/4. Should have company name/logo on the front "KGV Lending Corp." or Corporation whichever looks better
MarlaHenson.example MarlaHensonRE.example KGVLending.example
Home Loans & Real Estate Investments,
Mortgage Broker, Licensed Real Estate Broker,
California Certified Residential Property Manager (CPM),
Short Sale & Foreclosure Resource Certified (SFR),
BS Business Admin., University of Brookhollow, CA

```html
<!DOCTYPE html>
<html lang="en">
<head>
<meta charset="utf-8">
<title>KGV Mortgage &amp; Real Estate — Stationery</title>
<link rel="stylesheet" href="https://fonts.googleapis.com/css2?family=Open+Sans:wght@400;600;700&display=swap">
<style>
  :root {
    --ink: #231f20;
    --grey: #4a4a4a;
    --light-grey: #c9c9c9;
    --faint: #efefef;
    --blue: #2b3990;
    --orange: #f26522;
    --paper: #ffffff;
    --edge: #bdbdbd;
  }
  * { margin: 0; padding: 0; box-sizing: border-box; }
  html, body { width: 1200px; height: 742px; overflow: hidden; background: var(--paper); }
  body { position: relative; font-family: "Open Sans", Arial, sans-serif; color: var(--ink); }

  .sheet, .envelope { position: absolute; background: var(--paper); border: 1px solid var(--edge); overflow: hidden; }
  .sheet { left: 29px; top: 29px; width: 538px; height: 686px; }
  .envelope { left: 595px; top: 211px; width: 577px; height: 258px; border-top: none; }
  .envelope-flap { position: absolute; left: 595px; top: 145px; }

  .accent-bar { position: absolute; left: 4px; width: 4px; }
  .bar-black { background: var(--ink); }
  .bar-blue { background: var(--blue); }
  .bar-orange { background: var(--orange); }

  .brand { position: absolute; display: flex; align-items: center; gap: 8px; }
  .brand-dot { width: 12px; height: 12px; border-radius: 50%; background: var(--orange); flex: none; }
  .brand-name { font-weight: 600; color: var(--ink); line-height: 1.15; letter-spacing: 0.3px; }

  .sheet .brand { left: 28px; top: 60px; }
  .sheet .brand-name { font-size: 21px; }
  .envelope .brand { left: 20px; top: 30px; }
  .envelope .brand-name { font-size: 17px; }

  .faint-mark { position: absolute; font-weight: 600; color: var(--faint); letter-spacing: 2px; line-height: 1; user-select: none; }
  .sheet .faint-mark { left: 112px; top: 560px; font-size: 88px; }
  .envelope .faint-mark { left: 410px; top: 72px; font-size: 56px; }

  .signatory { position: absolute; left: 392px; top: 110px; }
  .signatory-name { font-size: 17px; font-weight: 600; color: var(--grey); }
  .signatory-title { font-size: 11px; color: var(--grey); margin-top: 2px; }

  .address { position: absolute; font-weight: 700; color: var(--ink); }
  .contact { position: absolute; display: flex; justify-content: space-between; font-size: 8.5px; color: var(--grey); white-space: nowrap; }
  .contact b { color: var(--ink); margin-right: 8px; }
  .contact .sep { color: var(--light-grey); }

  .sheet .address { left: 20px; top: 648px; font-size: 13px; }
  .sheet .contact { left: 20px; top: 668px; width: 500px; }
  .envelope .address { left: 22px; top: 212px; font-size: 12.5px; }
  .envelope .contact { left: 22px; top: 232px; width: 535px; }
</style>
</head>
<body>

<section class="sheet letterhead" aria-label="Letterhead">
  <div class="accent-bar bar-black" style="top:0;height:211px"></div>
  <div class="accent-bar bar-blue" style="top:211px;height:228px"></div>
  <div class="accent-bar bar-orange" style="top:439px;height:247px"></div>

  <div class="brand">
    <span class="brand-dot"></span>
    <span class="brand-name">KGV Mortgage &amp;<br>Real Estate</span>
  </div>

  <div class="signatory">
    <p class="signatory-name">Marla Henson</p>
    <p class="signatory-title">Broker / Owner</p>
  </div>

  <div class="faint-mark" aria-hidden="true">KGV</div>

  <p class="address">246 W. "K" Avenue, Cedarmont CA 91704</p>
  <p class="contact">
    <span><b>Phone</b>555-010-0134</span><span class="sep">|</span>
    <span><b>Cell</b>555-010-0178</span><span class="sep">|</span>
    <span><b>Fax</b>555-010-0192</span><span class="sep">|</span>
    <span><b>Email</b>MarlaHenson@quillmail.example</span>
  </p>
</section>

<svg class="envelope-flap" width="577" height="67" viewBox="0 0 577 67" aria-hidden="true">
  <polygon points="12,0 577,0 577,67 0,67" fill="#231f20"/>
</svg>

<section class="envelope" aria-label="Envelope">
  <div class="accent-bar bar-black" style="top:0;height:100px"></div>
  <div class="accent-bar bar-blue" style="top:100px;height:72px"></div>
  <div class="accent-bar bar-orange" style="top:172px;height:72px"></div>

  <div class="brand">
    <span class="brand-dot"></span>
    <span class="brand-name">KGV Mortgage &amp;<br>Real Estate</span>
  </div>

  <div class="faint-mark" aria-hidden="true">KGV</div>

  <p class="address">246 W. "K" Avenue, Cedarmont CA 91704</p>
  <p class="contact">
    <span><b>Phone</b>555-010-0134</span><span class="sep">|</span>
    <span><b>Cell</b>555-010-0178</span><span class="sep">|</span>
    <span><b>Fax</b>555-010-0192</span><span class="sep">|</span>
    <span><b>Email</b>MarlaHenson@quillmail.example</span>
  </p>
</section>

</body>
</html>
```